10' Banner for Pest Control Company

I need a 10'x10' banner created for a Pest Control Company named, Brightfield Pest Control. It is a total service company so equal emphasis needs to be placed on bugs, termites, rodents, weeds, and tree services like Olive Tree spraying for fruit suppression. The main colors are Orange and Grey. This will be a banner for use at trade shows. It needs to show a customer at a glance exactly what we do and what our name is.
Our website is under development at http://dev.marlowbeck-example.com so you can visit there and get an idea of the colors used.
Thank you!
Updates

Project Deadline Extended
Reason: Deadline extended per some designer's requests.

Target Market(s)

People looking for pest control services in Phoenix, Arizona

Industry/Entity Type

Pest Control

Requirements
Must have
• Photos of pests.. bugs, rodents, termites, weeds, tree spraying
• Large logo
• Vibrant and eye catching

```html
<!DOCTYPE html>
<html lang="en">
<head>
<meta charset="utf-8">
<title>Brightfield Pest Control – Trade Show Banner</title>
<link href="https://fonts.googleapis.com/css2?family=Open+Sans:wght@400;600;700;800&display=swap" rel="stylesheet">
<style>
  :root {
    --orange: #df5a18;
    --orange-deep: #c94c12;
    --orange-soft: #e8733a;
    --white: #ffffff;
    --grey: #808080;
    --grey-dark: #5f5f5f;
  }
  * { margin: 0; padding: 0; box-sizing: border-box; }
  html, body { width: 1200px; height: 1200px; overflow: hidden; }
  body {
    font-family: "Open Sans", Arial, sans-serif;
    background: var(--orange);
    color: var(--white);
  }
  .banner {
    position: relative;
    width: 1200px;
    height: 1200px;
    overflow: hidden;
    background: var(--orange);
  }
  .backdrop {
    position: absolute;
    inset: 0;
    background:
      radial-gradient(ellipse 420px 300px at 560px 520px, rgba(90,40,20,0.22), transparent 70%),
      radial-gradient(ellipse 300px 200px at 900px 760px, rgba(90,40,20,0.18), transparent 70%),
      radial-gradient(ellipse 500px 400px at 200px 900px, rgba(255,140,80,0.12), transparent 70%),
      linear-gradient(160deg, var(--orange-soft) 0%, var(--orange) 45%, var(--orange-deep) 100%);
  }
  .headline {
    position: absolute;
    left: 76px;
    top: 92px;
    font-weight: 700;
    font-size: 80px;
    line-height: 86px;
    letter-spacing: 0.5px;
  }
  .intro {
    position: absolute;
    left: 84px;
    top: 318px;
    font-weight: 400;
    font-size: 45px;
    line-height: 56px;
  }
  .services {
    position: absolute;
    left: 76px;
    top: 462px;
    display: grid;
    grid-template-columns: 442px auto;
    row-gap: 38px;
    list-style: none;
    font-weight: 700;
    font-size: 44px;
    line-height: 48px;
  }
  .services li {
    display: flex;
    align-items: center;
    gap: 16px;
  }
  .services svg { width: 34px; height: 34px; flex: none; }
  .gallery {
    position: absolute;
    left: 72px;
    top: 693px;
    display: flex;
    gap: 10px;
  }
  .gallery .tile {
    width: 200px;
    height: 262px;
    border: 7px solid var(--white);
    border-radius: 24px;
    transform: skewX(-4deg);
    box-shadow: 0 2px 8px rgba(0,0,0,0.25);
  }
  .tile--roaches { background: linear-gradient(135deg, #8a5a2a, #c07a3a 50%, #2f4a3a); }
  .tile--termite { background: linear-gradient(135deg, #2c2f33, #c9a23f 55%, #e2e09a); }
  .tile--rodent { background: linear-gradient(135deg, #4a4a4a, #8c8c8c 50%, #6b5a48); }
  .tile--weeds { background: linear-gradient(135deg, #6f9a4a, #3f7a2e 55%, #9aa090); }
  .tile--spraying { background: linear-gradient(135deg, #5e8a3a, #eef0f2 50%, #3c6a2a); }
  .footer-shape {
    position: absolute;
    left: 0;
    top: 1010px;
    width: 1200px;
    height: 150px;
  }
  .phone {
    position: absolute;
    left: 71px;
    top: 1096px;
    font-weight: 600;
    font-size: 45px;
    line-height: 60px;
    color: var(--orange);
  }
  .brand {
    position: absolute;
    left: 792px;
    top: 1024px;
    display: flex;
    align-items: center;
    gap: 16px;
    color: var(--grey-dark);
    font-weight: 800;
    font-size: 50px;
    line-height: 58px;
    white-space: nowrap;
  }
  .brand-dot {
    width: 28px;
    height: 28px;
    border-radius: 50%;
    background: var(--orange);
    flex: none;
  }
</style>
</head>
<body>
<main class="banner">
  <div class="backdrop" role="img" aria-label="Faint photo of a large insect blended into the orange background"></div>

  <h1 class="headline">Safe and effective<br>pest control solutions</h1>

  <p class="intro">We offer a range of building and<br>pest inspection services</p>

  <ul class="services">
    <li><svg viewBox="0 0 34 34"><circle cx="17" cy="17" r="11" fill="none" stroke="#fff" stroke-width="2.5"/><circle cx="17" cy="17" r="3.5" fill="#fff"/><path d="M17 2v8M17 24v8M2 17h8M24 17h8" stroke="#fff" stroke-width="2.5"/></svg>Pest control</li>
    <li><svg viewBox="0 0 34 34"><circle cx="17" cy="17" r="11" fill="none" stroke="#fff" stroke-width="2.5"/><circle cx="17" cy="17" r="3.5" fill="#fff"/><path d="M17 2v8M17 24v8M2 17h8M24 17h8" stroke="#fff" stroke-width="2.5"/></svg>Custom spray services</li>
    <li><svg viewBox="0 0 34 34"><circle cx="17" cy="17" r="11" fill="none" stroke="#fff" stroke-width="2.5"/><circle cx="17" cy="17" r="3.5" fill="#fff"/><path d="M17 2v8M17 24v8M2 17h8M24 17h8" stroke="#fff" stroke-width="2.5"/></svg>Termite control</li>
    <li><svg viewBox="0 0 34 34"><circle cx="17" cy="17" r="11" fill="none" stroke="#fff" stroke-width="2.5"/><circle cx="17" cy="17" r="3.5" fill="#fff"/><path d="M17 2v8M17 24v8M2 17h8M24 17h8" stroke="#fff" stroke-width="2.5"/></svg>Weed control</li>
  </ul>

  <div class="gallery">
    <div class="tile tile--roaches" role="img" aria-label="Photo of cockroaches on a branch"></div>
    <div class="tile tile--termite" role="img" aria-label="Close-up photo of a termite soldier"></div>
    <div class="tile tile--rodent" role="img" aria-label="Photo of a grey rodent"></div>
    <div class="tile tile--weeds" role="img" aria-label="Photo of a dandelion weed growing on paving"></div>
    <div class="tile tile--spraying" role="img" aria-label="Photo of a technician in protective gear spraying olive trees"></div>
  </div>

  <svg class="footer-shape" viewBox="0 0 1200 150" preserveAspectRatio="none" aria-hidden="true">
    <path d="M0 92 H690 C720 92 730 84 745 60 L770 16 C778 4 786 0 800 0 H1200 V147 H0 Z" fill="#fff"/>
  </svg>

  <div class="phone">Call: +1 602 555 0188</div>

  <div class="brand">
    <span class="brand-dot"></span>
    <span>Brightfield<br>Pest Control</span>
  </div>
</main>
</body>
</html>
```